Full page ad in a magazine

We would like an ad designed to be placed for advertising in magazines, theater playbills, etc. I have attached a copy of some previous ads that were done for us, although they need much improvement and redesigned. We have won "best chiropractor" awards that can be seen on our website home page at harlowspineandjoint.example

```html
<!DOCTYPE html>
<html lang="en">
<head>
<meta charset="utf-8">
<title>Harlow Spine &amp; Joint Center – Magazine Ad</title>
<link rel="stylesheet" href="https://fonts.googleapis.com/css2?family=Quicksand:wght@300;400;500;600;700&display=swap">
<style>
  :root {
    --brand-red: #b21f25;
    --ink: #1c1c1c;
    --black-band: #111111;
    --paper: #ffffff;
    --mist-dark: #bdbdbd;
    --photo-light: #d4d4d4;
    --photo-dark: #a9a9a9;
    --badge-blue: #2e4f9a;
    --badge-orange: #f0962a;
    --badge-teal: #3cc4b8;
  }
  * { box-sizing: border-box; margin: 0; padding: 0; }
  html, body { width: 1000px; height: 1200px; overflow: hidden; background: #ffffff; }
  body { font-family: "Quicksand", sans-serif; color: var(--ink); }

  .ad { position: relative; width: 1000px; height: 1200px; overflow: hidden; background: var(--paper); }

  .hero-backdrop { position: absolute; left: 0; top: 0; width: 1000px; height: 674px; }

  .hero-photo {
    position: absolute; left: 640px; top: 230px; width: 360px; height: 444px;
    background: linear-gradient(to bottom, var(--photo-light) 0%, var(--photo-dark) 100%);
  }

  .brand { position: absolute; left: 51px; top: 50px; display: flex; align-items: center; gap: 16px; }
  .brand-mark { width: 104px; height: 115px; background: var(--mist-dark); border: 2px solid #555; }
  .brand-name { font-weight: 700; font-size: 42px; line-height: 1.08; color: var(--brand-red); letter-spacing: 0.5px; }

  .headline { position: absolute; left: 46px; top: 266px; font-size: 61px; font-weight: 700; letter-spacing: -0.3px; color: var(--ink); line-height: 1; }
  .services { position: absolute; left: 47px; top: 361px; font-size: 43px; font-weight: 700; color: var(--brand-red); line-height: 1; }

  .treating-tag {
    position: absolute; left: 47px; top: 453px; width: 150px; height: 45px;
    background: var(--brand-red); color: #fff; font-size: 25px; font-weight: 500;
    line-height: 45px; padding-left: 11px;
    clip-path: polygon(0 0, 93% 0, 100% 50%, 93% 100%, 0 100%);
  }
  .conditions { position: absolute; top: 439px; list-style: none; font-size: 29px; font-weight: 500; line-height: 46.5px; color: var(--ink); }
  .conditions--left { left: 221px; }
  .conditions--right { left: 436px; }
  .conditions-divider { position: absolute; left: 409px; top: 450px; width: 2px; height: 116px; background: var(--brand-red); }

  .insurance { position: absolute; left: 47px; top: 598px; font-size: 34px; font-weight: 300; color: #333; }

  .doctor-band { position: absolute; left: 0; top: 674px; width: 1000px; height: 223px; background: var(--brand-red); }
  .doctor-name-bar {
    position: absolute; left: 0; top: 833px; width: 668px; height: 64px;
    background: var(--black-band); border-top-right-radius: 64px;
  }
  .doctor-photo {
    position: absolute; left: 44px; top: 674px; width: 274px; height: 223px;
    background: linear-gradient(135deg, #6b6e74 0%, #4c4f55 55%, #3a3c40 100%);
  }
  .vote-text { position: absolute; left: 346px; top: 693px; color: #fff; font-weight: 700; }
  .vote-line { font-size: 35px; line-height: 44px; }
  .vote-url { font-size: 23px; line-height: 30px; }
  .doctor-name { position: absolute; left: 346px; top: 842px; font-size: 35px; font-weight: 700; color: #fff; }

  .award-badge {
    position: absolute; left: 789px; top: 707px; width: 179px; height: 150px;
    background: linear-gradient(to bottom, var(--badge-orange) 0 24%, var(--badge-blue) 24% 73%, var(--badge-teal) 73% 100%);
  }
  .award-caption { position: absolute; left: 778px; top: 862px; width: 199px; text-align: center; font-size: 18px; font-weight: 500; color: #fff; }

  .contact-icon { position: absolute; width: 40px; height: 40px; }
  .contact-icon--phone { left: 45px; top: 961px; }
  .contact-icon--home { left: 564px; top: 961px; }

  .phone-number { position: absolute; left: 102px; top: 940px; font-size: 64px; font-weight: 700; color: var(--ink); letter-spacing: 0.5px; }
  .hours { position: absolute; left: 103px; top: 1012px; font-size: 27px; font-weight: 700; color: var(--brand-red); }

  .location { position: absolute; left: 625px; top: 953px; color: var(--ink); font-style: normal; }
  .location-title { font-size: 26px; font-weight: 700; line-height: 32px; }
  .location-line { font-size: 25px; font-weight: 500; line-height: 30px; }

  .footer-band {
    position: absolute; left: 0; top: 1104px; width: 1000px; height: 96px; background: var(--brand-red);
    display: flex; align-items: center; justify-content: center; gap: 16px;
  }
  .footer-url { font-size: 29px; font-weight: 700; color: #fff; letter-spacing: 0.3px; }
</style>
</head>
<body>
<main class="ad">

  <svg class="hero-backdrop" viewBox="0 0 1000 674" aria-hidden="true">
    <defs>
      <linearGradient id="mistFill" x1="0" y1="0" x2="1" y2="0">
        <stop offset="0" stop-color="#dcdcdc"/>
        <stop offset="0.45" stop-color="#f6f6f6"/>
        <stop offset="1" stop-color="#d6d6d6"/>
      </linearGradient>
    </defs>
    <rect width="1000" height="674" fill="url(#mistFill)"/>
    <path d="M0 0 H790 C720 140 560 218 300 222 L0 224 Z" fill="#c8c8c8"/>
    <path d="M0 0 H778 C710 130 555 208 300 212 L0 214 Z" fill="#ffffff"/>
  </svg>

  <div class="hero-photo" role="img" aria-label="Photo of a man from behind holding his neck and lower back, with the pain areas highlighted in red"></div>

  <header class="brand">
    <span class="brand-mark" aria-hidden="true"></span>
    <span class="brand-name">HARLOW SPINE<br>&amp; JOINT CENTER</span>
  </header>

  <h1 class="headline">Neck or Back Pain ?</h1>
  <p class="services">CHIROPRACTIC • MASSAGE</p>

  <div class="treating-tag">TREATING:</div>
  <ul class="conditions conditions--left">
    <li>BACK PAIN</li>
    <li>NECK PAIN</li>
    <li>HEADACHES</li>
  </ul>
  <span class="conditions-divider" aria-hidden="true"></span>
  <ul class="conditions conditions--right">
    <li>JOINT PAIN</li>
    <li>SCIATICA</li>
    <li>FATIGUE</li>
  </ul>

  <p class="insurance">Medicare and most Insurance accepted</p>

  <section class="doctor-band" aria-label="Vote for us"></section>
  <div class="doctor-name-bar" aria-hidden="true"></div>
  <div class="doctor-photo" role="img" aria-label="Portrait photo of the chiropractor in a grey suit and tie"></div>
  <div class="vote-text">
    <p class="vote-line">Vote for us:</p>
    <p class="vote-line">Best Chiropractor</p>
    <p class="vote-url">www.regionmedia.example/bestof</p>
  </div>
  <p class="doctor-name">Martin Keller, DC</p>

  <div class="award-badge" aria-hidden="true"></div>
  <p class="award-caption">Greater Harlow</p>

  <svg class="contact-icon contact-icon--phone" viewBox="0 0 40 40" aria-hidden="true">
    <circle cx="20" cy="20" r="18" fill="none" stroke="var(--brand-red)" stroke-width="2.5"/>
    <path d="M13.5 11.5 l4 -1 l2 5 l-2.5 1.8 c1 2.5 3 4.5 5.5 5.5 l1.8 -2.5 l5 2 l-1 4 c-9 1 -16 -6 -14.8 -14.8 z" fill="var(--brand-red)"/>
  </svg>
  <p class="phone-number">555.014.2736</p>
  <p class="hours">OPEN MONDAY - SATURDAY</p>

  <svg class="contact-icon contact-icon--home" viewBox="0 0 40 40" aria-hidden="true">
    <circle cx="20" cy="20" r="18" fill="none" stroke="var(--brand-red)" stroke-width="2.5"/>
    <path d="M20 10 L30 19 H27 V29 H22.5 V23 H17.5 V29 H13 V19 H10 Z" fill="var(--brand-red)"/>
  </svg>
  <address class="location">
    <p class="location-title">LINDEN PARK LOCATION</p>
    <p class="location-line">120 Linden Court St., #204</p>
    <p class="location-line">Harlow, VA 20100</p>
  </address>

  <footer class="footer-band">
    <svg width="36" height="36" viewBox="0 0 36 36" aria-hidden="true">
      <circle cx="18" cy="18" r="16.5" fill="none" stroke="#fff" stroke-width="2"/>
      <circle cx="18" cy="18" r="10" fill="none" stroke="#fff" stroke-width="2"/>
      <ellipse cx="18" cy="18" rx="4.5" ry="10" fill="none" stroke="#fff" stroke-width="1.6"/>
      <line x1="8" y1="18" x2="28" y2="18" stroke="#fff" stroke-width="1.6"/>
    </svg>
    <span class="footer-url">HARLOWSPINEANDJOINT.EXAMPLE</span>
  </footer>

</main>
</body>
</html>
```